Rock, Paper Scissors Championship Flyer

We need a dynamic, bold and exciting flyer to promote the following event at our sports center. The event will be primarily focused for adults, but children are welcome to join

Rock, Paper, Scissors Championship - $$$ prizes
Date: June 9th, 2018
Time: 11am-4pm
Fee: $2 to enter, free for spectators
Heats to determine the overall ‘Rock, Paper, Scissors’ champion!
- Cash prizes on offer
- Live music.
- Food and beverage available for purchase

Belvorrow Sports Center, Roselle NJ
908-555-3162
www.belvorrowgrounds.example

Must include our logo (does not have to be huge) and County seal (both attached)

Colors

Designer to choose colors to be used in the design.

Requirements
Must have
• Should be fun and colorful
• The following info and attached logos:
• Rock, Paper, Scissors Championship - $$$ prizes
• Date: June 9th, 2018
• Time: 11am-4pm
• Fee: $2 to enter, free for spectators
• Heats to determine the overall ‘Rock, Paper, Scissors’ champion!
• - Cash prizes on offer
• - Live music.
• - Food and beverage available for purchase
• Belvorrow Sports Center, Roselle NJ
• 908-555-3162
• www.belvorrowgrounds.example
Nice to have
• There are a few inspirational photos attached to give an idea of what we are looking for.

```html
<!DOCTYPE html>
<html lang="en">
<head>
<meta charset="utf-8">
<title>Rock, Paper, Scissors Championship</title>
<link rel="stylesheet" href="https://fonts.googleapis.com/css2?family=Bubblegum+Sans&family=Domine:wght@700&display=swap">
<style>
  :root {
    --navy: #1c4472;
    --navy-deep: #163a63;
    --lime: #8cc63f;
    --lime-band: #8dc63f;
    --green-dark: #1f8a3a;
    --white: #ffffff;
    --ink-navy: #173a66;
    --gray: #555a60;
    --photo-warm: #8a6a52;
    --photo-cool: #3d5573;
  }
  * { margin: 0; padding: 0; box-sizing: border-box; }
  html, body { width: 782px; height: 1200px; overflow: hidden; background: #ffffff; }
  .flyer {
    position: relative;
    width: 782px;
    height: 1200px;
    background: var(--white);
    overflow: hidden;
    font-family: "Domine", Georgia, serif;
  }
  .hero-photo {
    position: absolute;
    left: 0; top: 0;
    width: 782px; height: 520px;
    background: linear-gradient(160deg, #b79b7e 0%, var(--photo-warm) 35%, #6d7f96 65%, var(--photo-cool) 100%);
  }
  .navy-panel {
    position: absolute;
    left: 0; top: 0;
    width: 782px; height: 947px;
  }
  .county-seal {
    position: absolute;
    left: 35px; top: 6px;
    width: 76px; height: 76px;
    border-radius: 50%;
    background: #d9b860;
    border: 4px solid #2b4a2a;
  }
  .title {
    position: absolute;
    left: 0; right: 0; top: 612px;
    text-align: center;
    font-family: "Bubblegum Sans", "Comic Sans MS", cursive;
    color: var(--lime);
    font-size: 62px;
    line-height: 64px;
    letter-spacing: 1px;
    text-transform: uppercase;
  }
  .event-time {
    position: absolute;
    left: 0; right: 0; top: 772px;
    text-align: center;
    color: var(--white);
    font-size: 37px;
  }
  .fee-pill {
    position: absolute;
    left: 83px; top: 842px;
    width: 618px; height: 52px;
    border: 2px solid #cfd8e4;
    border-radius: 12px;
    box-shadow: 0 4px 6px rgba(0,0,0,0.35);
    display: flex; align-items: center; justify-content: center;
    font-size: 27px;
    color: var(--white);
    text-transform: uppercase;
  }
  .fee-pill .fee { color: var(--lime); margin-right: 10px; }
  .features {
    position: absolute;
    left: 0; right: 0; top: 968px;
    text-align: center;
    color: var(--ink-navy);
    font-size: 29px;
    line-height: 38px;
  }
  .cta {
    position: absolute;
    left: 0; right: 0; top: 1058px;
    text-align: center;
    color: var(--green-dark);
    font-size: 29px;
    text-transform: uppercase;
  }
  .contact-band {
    position: absolute;
    left: 0; top: 1103px;
    width: 782px; height: 51px;
    background: var(--lime-band);
    color: var(--white);
    font-size: 29px;
    display: flex; align-items: center; justify-content: center;
  }
  .venue {
    position: absolute;
    left: 0; right: 0; top: 1162px;
    text-align: center;
    color: var(--gray);
    font-size: 18px;
  }
</style>
</head>
<body>
<main class="flyer">
  <div class="hero-photo" role="img" aria-label="Photo of four young friends on a sofa playing rock, paper, scissors in front of bookshelves"></div>
  <svg class="navy-panel" viewBox="0 0 782 947" aria-hidden="true">
    <path fill="#1c4472" d="M0 445 L20 452 L45 470 L80 488 L120 500 L170 505 L220 512 L260 515 L300 508 L340 518 L380 512 L420 520 L460 510 L500 515 L540 505 L580 512 L620 500 L660 505 L700 490 L730 478 L760 462 L782 450 L782 947 L0 947 Z"/>
  </svg>
  <div class="county-seal" aria-hidden="true"></div>
  <h1 class="title">Rock, Paper, Scissors<br>Championship</h1>
  <p class="event-time">June 9th, 2018 Time: 11am-4pm</p>
  <p class="fee-pill"><span class="fee">$2 to enter,</span> free for spectators</p>
  <p class="features">Cash prizes on offer | Live music.<br>Food and beverage available for purchase</p>
  <p class="cta">Contact us today</p>
  <p class="contact-band">908-555-3162 &nbsp;|&nbsp; www.belvorrowgrounds.example</p>
  <p class="venue">Belvorrow Sports Center, Roselle NJ</p>
</main>
</body>
</html>
```